Letterhead, card design, stationary, etc
Marlowe Dental Group
I need double sided standard sized Business Card [3.5" x 2"]
No specifications
Professional
Nathaniel J. Brackett DDS, FAGD
Cosmetic and Comprehensive Dentistry
41736 Marlowe Ridge Rd.
Suite 385
Golden, CO 80517
marlowe@plimnetmail.net
www.marlowedentalgroup.com
Use a design which could be used on white or black stock (background)...
A space to write appointment times, etc...
Logo
Small Logo

```html
<!DOCTYPE html>
<html lang="en">
<head>
<meta charset="utf-8">
<title>Marlowe Dental Group Stationery</title>
<link href="https://fonts.googleapis.com/css2?family=Open+Sans:wght@400;600;700&display=swap" rel="stylesheet">
<style>
:root{
  --bg:#e9e6e0;
  --paper:#ffffff;
  --green:#3f7d2c;
  --green-dark:#2c5e1d;
  --green-light:#7fb24a;
  --ink:#555;
  --rule:#c9c9c9;
}
*{box-sizing:border-box;margin:0;padding:0}
html,body{width:1200px;height:559px;overflow:hidden}
body{background:var(--bg);font-family:"Open Sans",Arial,sans-serif;color:var(--ink);position:relative}
.sheet{position:absolute;background:var(--paper);box-shadow:0 1px 4px rgba(0,0,0,.18)}
.brand{font-family:"Open Sans",Arial,sans-serif;font-weight:700;color:var(--green);line-height:1.1;display:flex;align-items:center;gap:4px;white-space:nowrap}
.brand .dot{display:inline-block;flex:none;border-radius:50%;background:var(--green)}
.address-block{position:absolute;width:96px;text-align:right;font-size:4px;line-height:1.5;color:#777}
.footer-band{position:absolute;left:0;right:0;bottom:0;height:14px;background:linear-gradient(var(--green-light),var(--green))}
.footer-text{position:absolute;bottom:17px;left:14px;right:14px;display:flex;justify-content:space-between;font-size:4px;color:var(--green)}
/* fax and letterhead */
.fax{left:77px;top:24px;width:259px;height:480px}
.letterhead{left:348px;top:24px;width:259px;height:480px}
.sheet .brand.top{position:absolute;left:14px;top:14px;font-size:9px}
.sheet .address-block.top{right:14px;top:12px}
.fax-title{position:absolute;left:16px;top:62px;font-weight:700;color:var(--green);font-size:14px}
.fax-fields{position:absolute;left:16px;top:96px;width:227px;display:grid;grid-template-columns:1fr 1fr;column-gap:12px;row-gap:7px;font-size:5px;color:#666}
.fax-fields span{border-bottom:1px solid var(--rule);padding-bottom:2px}
.fax-checks{position:absolute;left:16px;top:165px;width:227px;display:flex;justify-content:space-between;font-size:4.4px}
.fax-checks span::before{content:"";display:inline-block;width:4px;height:4px;border:1px solid var(--green);border-radius:50%;margin-right:2px;vertical-align:-1px}
/* envelope */
.envelope-back{left:720px;top:24px;width:336px;height:132px;overflow:hidden}
.envelope-front{left:720px;top:168px;width:336px;height:132px}
.flap{position:absolute;left:0;top:0;width:100%;height:64px}
.envelope-back .brand{position:absolute;left:0;right:0;top:8px;justify-content:center;font-size:8px;color:#fff}
.envelope-back .return{position:absolute;left:0;right:0;top:70px;justify-content:center;font-size:8px}
.envelope-front .brand{position:absolute;left:14px;top:14px;font-size:8px}
.envelope-front .sender{position:absolute;left:14px;top:78px;font-size:4.6px;line-height:1.5}
.envelope-front .footer-band{height:8px}
/* cards */
.card{width:96px;height:54px;border-radius:3px;overflow:hidden}
.card-front{left:960px;top:336px}
.card-front .brand{position:absolute;left:6px;top:6px;font-size:5px}
.card-front .info{position:absolute;left:6px;top:24px;font-size:3.2px;line-height:1.45;white-space:nowrap}
.card-front .info b{color:var(--green);font-weight:700}
.card-front .footer-band{height:5px}
.appointment{left:840px;top:410px;width:96px;height:84px;border-radius:3px}
.appointment h3{position:absolute;left:8px;top:10px;font-size:5px;font-weight:700;color:var(--green)}
.appointment .lines{position:absolute;left:8px;right:8px;top:22px}
.appointment .lines span{display:block;border-bottom:1px solid var(--rule);height:9px;font-size:3.4px;color:#888}
.appointment .footer-band{height:6px}
.map-card{left:948px;top:404px;width:120px;height:90px;border-radius:3px;overflow:hidden}
.map-card h3{position:absolute;right:8px;top:8px;font-size:5px;font-weight:700;color:var(--green)}
.map-area{position:absolute;left:6px;top:18px;width:108px;height:56px;background:linear-gradient(135deg,#f3ece2,#f6d9d3 55%,#e8efe2)}
.map-card .footer-band{height:6px}
</style>
</head>
<body>

<section class="sheet fax">
  <div class="brand top"><span class="dot" style="width:6px;height:6px"></span><span>Marlowe<br>Dental Group</span></div>
  <div class="address-block top">41736 Marlowe Ridge Rd. Suite 385<br>Golden, CO 80517<br>Phone (303) 555-0187 &nbsp; Fax (303) 555-0188<br>marlowe@plimnetmail.net<br>www.marlowedentalgroup.com</div>
  <div class="fax-title">FAX</div>
  <div class="fax-fields">
    <span>To:</span><span>From:</span>
    <span>Fax:</span><span>Pages:</span>
    <span>Phone:</span><span>Date:</span>
    <span>Re:</span><span>CC:</span>
  </div>
  <div class="fax-checks">
    <span>Urgent</span><span>For Review</span><span>Please Comment</span><span>Please Reply</span><span>Please Recycle</span>
  </div>
  <div class="footer-text"><span>www.marlowedentalgroup.com</span><span>marlowe@plimnetmail.net</span></div>
  <div class="footer-band"></div>
</section>

<section class="sheet letterhead">
  <div class="brand top"><span class="dot" style="width:6px;height:6px"></span><span>Marlowe<br>Dental Group</span></div>
  <div class="address-block top">41736 Marlowe Ridge Rd. Suite 385<br>Golden, CO 80517<br>Phone (303) 555-0187 &nbsp; Fax (303) 555-0188<br>marlowe@plimnetmail.net<br>www.marlowedentalgroup.com</div>
  <div class="footer-text"><span>www.marlowedentalgroup.com</span><span>marlowe@plimnetmail.net</span></div>
  <div class="footer-band"></div>
</section>

<section class="sheet envelope-back">
  <svg class="flap" viewBox="0 0 336 64" preserveAspectRatio="none" aria-hidden="true">
    <defs><linearGradient id="flapFill" x1="0" y1="0" x2="0" y2="1"><stop offset="0" stop-color="#7fb24a"/><stop offset="1" stop-color="#2c5e1d"/></linearGradient></defs>
    <path d="M0 0H336V22Q168 70 0 22Z" fill="url(#flapFill)"/>
  </svg>
  <div class="brand"><span class="dot" style="width:5px;height:5px;background:#fff"></span><span>Marlowe<br>Dental Group</span></div>
  <div class="brand return"><span class="dot" style="width:5px;height:5px"></span><span>Marlowe<br>Dental Group</span></div>
</section>

<section class="sheet envelope-front">
  <div class="brand"><span class="dot" style="width:5px;height:5px"></span><span>Marlowe<br>Dental Group</span></div>
  <div class="sender">41736 Marlowe Ridge Rd.<br>Suite 385<br>Golden, CO 80517</div>
  <div class="footer-band"></div>
</section>

<section class="sheet card card-front">
  <div class="brand"><span class="dot" style="width:4px;height:4px"></span><span>Marlowe<br>Dental Group</span></div>
  <div class="info"><b>Nathaniel J. Brackett DDS, FAGD</b><br>Cosmetic and Comprehensive Dentistry<br>41736 Marlowe Ridge Rd. Suite 385<br>Golden, CO 80517 · (303) 555-0187<br>www.marlowedentalgroup.com</div>
  <div class="footer-band"></div>
</section>

<section class="sheet appointment">
  <h3>Appointment</h3>
  <div class="lines"><span>Name</span><span>Date</span><span>Time</span><span>Day</span></div>
  <div class="footer-band"></div>
</section>

<section class="sheet map-card">
  <h3>Appointment</h3>
  <div class="map-area" role="img" aria-label="Street map showing the route to the dental office"></div>
  <div class="footer-band"></div>
</section>

</body>
</html>
```